Trellform482 - Platform for Digitalisation - Web Page

Trellform482 is a web based platform for process modelling, process automation, task management and tool integration. We keep processes and tools in sync. The current webpage is https://www.trellform482.example

Trellform482 is the auto pilot for your organisation. Like in an airplane Trellform482 ensures that the processes are running. On our platform you

- first model your processes in the online process editor
- then you automate them with a single click (no coding required)
- then you integrate your tools (like Vondrel Kestik, Halvern Relaymark, taskwharf, Pellunar, Cartisle, Bromm, Tazzo, ...)

The platform provides the functionality in varous apps (e.g. Process Management, Task Management, Data Exchange, CRM, Project Management). For each app we will have at least one page that describes the app features (kind of a landing page).

The app can have a sub section. For example, the Data Exchange app (this is the app that syncs tools) has various adapters. For example: Vondrel Kestik, taskwharf, QDL Fennel - WQP, QDL Fennel - GATES KT, Halvern Quorbit BuildOps, Bromm, Tazzo, PingDrift, Halvern Relaymark, ...). Each adapter will be presented on an individual page.

We need a Theme for our new website (preferably Wordpress). The website will contain the following sections:
- Home (you could compare it to the Quince Toolbazaar - where some apps are featured, some things highlighted, the product is explained in a video).
- One page per app (probably each app will have a slightly different coloring)
- One page per sub section (e.g. Adapter)

Our web based application is currently using JSF with CoreTiles. Our mobile app is built with React Native.

The following page is one of the pages I like:
https://www.fetchlumo.example/

A good example is https://plorivo.example/.
They provide "Templates" which is comparable to the apps and adapters in Trellform482.

Target Market(s)

CIO, CTO

Industry/Entity Type

It Company

Coding

Coded - Design and coding required

Number of Pages Required

4 page

Font styles to use
Sans Serif

Colors

Designer to choose colors to be used in the design.

Requirements
Must have
• Separate Design for
• - Index Page (kind of an App Store welcome page)
• - App Page (for each app - each of them will have an individual color - for example in the header section)
• - Adapter Page
• - Pricing table
Nice to have
• - Contact Form Page

```html
<!DOCTYPE html>
<html lang="en">
<head>
<meta charset="utf-8">
<title>Trellform482 – Platform for Digitalisation</title>
<link href="https://fonts.googleapis.com/css2?family=Montserrat:wght@500;600;700;800&family=Open+Sans:wght@400;600;700&display=swap" rel="stylesheet">
<style>
:root{
  --blue-deep:#0b3279;
  --blue:#1a56b0;
  --blue-light:#3f86d8;
  --navy:#123a7a;
  --orange:#f5a746;
  --orange-dark:#ec8f22;
  --ink:#333a44;
  --muted:#6d7582;
  --white:#ffffff;
  --footer:#1e1f22;
  --footer-text:#c9cbd0;
  --field:rgba(255,255,255,.14);
}
*{box-sizing:border-box;margin:0;padding:0}
html,body{width:1200px;height:4455px;overflow:hidden}
body{font-family:"Open Sans",Arial,sans-serif;color:var(--ink);background:#fff;position:relative}
.page{position:relative;width:1200px;height:4455px;overflow:hidden}
.abs{position:absolute}
h1,h2,h3,.btn,.nav a,.logo{font-family:"Montserrat",Arial,sans-serif}
.btn{display:inline-block;border-radius:30px;font-weight:700;font-size:13px;letter-spacing:.5px;text-align:center;text-transform:uppercase;text-decoration:none}
.btn-outline{border:2px solid var(--navy);color:var(--navy);width:160px;height:44px;line-height:40px;background:#fff}
.logo{display:flex;align-items:center;gap:10px;color:#fff;font-weight:800;font-size:24px;letter-spacing:1px}
.logo .mark{width:40px;height:40px;border:4px solid #fff;border-radius:50%}

/* hero */
.hero-bg{left:0;top:0;width:1200px;height:640px;background:linear-gradient(120deg,#0a2b6b 0%,#1c5bb5 55%,#2f73c9 100%)}
.nav{left:580px;top:30px;display:flex;gap:42px}
.nav a{color:#fff;font-size:14px;font-weight:600;text-decoration:none;letter-spacing:.5px}
.nav a.active{border-bottom:2px solid #fff}
.hero-title{left:137px;top:203px;width:430px;color:#fff;font-size:30px;line-height:37px;font-weight:500;text-transform:uppercase;white-space:nowrap}
.hero-text{left:137px;top:322px;width:430px;color:#fff;font-size:14px;line-height:21px}
.hero-btns{left:137px;top:386px;display:flex;gap:20px}
.btn-white{background:#fff;color:var(--navy);width:158px;height:44px;line-height:44px}
.btn-orange{background:var(--orange);color:#fff;width:158px;height:44px;line-height:44px}
.hero-shot{left:585px;top:165px;width:410px;height:310px;background:linear-gradient(180deg,#eef1f5,#d9dee6);border-radius:6px;box-shadow:0 10px 30px rgba(0,0,0,.3)}
.hero-phone{left:955px;top:220px;width:120px;height:245px;background:linear-gradient(180deg,#2c3440,#121820);border-radius:18px;box-shadow:0 10px 25px rgba(0,0,0,.35)}
.slide-arrow{width:40px;height:40px;border-radius:50%;background:rgba(0,0,0,.55);display:flex;align-items:center;justify-content:center}

/* cards */
.card{top:590px;width:290px;height:315px;border-radius:10px;background:#fff;box-shadow:0 8px 24px rgba(20,40,80,.18);text-align:center;padding:28px 24px 0}
.card.is-featured{background:var(--orange);color:#fff}
.card svg{display:block;margin:0 auto 10px}
.card h3{font-size:16px;font-weight:700;text-transform:uppercase;color:var(--blue);margin-bottom:12px}
.card.is-featured h3{color:#fff}
.card p{font-size:13px;line-height:19px;color:var(--muted)}
.card.is-featured p{color:#fff}
.card .btn{position:absolute;left:50%;transform:translateX(-50%);bottom:30px;width:140px;height:32px;line-height:32px;font-size:12px;text-transform:none}
.card .btn-navy{background:var(--navy);color:#fff}
.card .btn-light{background:#fff;color:var(--navy)}

/* split sections */
.media{background:linear-gradient(135deg,#c9d3df,#8ea1b8);box-shadow:0 8px 24px rgba(0,0,0,.18)}
.split h2{font-size:24px;line-height:30px;font-weight:800;color:var(--blue-deep);text-transform:uppercase;margin-bottom:18px}
.split p{font-size:13.5px;line-height:21px;color:var(--ink);margin-bottom:22px}

/* features */
.features-title{left:0;top:1428px;width:1200px;text-align:center;color:#fff;font-size:28px;font-weight:800}
.feature{top:1525px;width:210px;text-align:center;color:#fff}
.feature h3{font-size:17px;line-height:20px;font-weight:700;margin:10px 0 8px}
.feature p{font-size:12px;line-height:16px;color:#aecbf0}

/* clients */
.clients-title{left:0;top:3258px;width:1200px;text-align:center;font-size:24px;line-height:31px;font-weight:800;color:#2b2f36;text-transform:uppercase}
.clients{left:180px;top:3370px;width:840px;display:flex;justify-content:space-between;align-items:center}
.clients span{font-family:"Montserrat",Arial,sans-serif;font-weight:700;font-size:22px;color:#3b3f46}

/* contact */
.contact-title{left:0;top:3638px;width:1200px;text-align:center;color:#fff;font-size:28px;font-weight:800}
.contact-intro{left:350px;top:3682px;width:500px;text-align:center;color:#a9c6ee;font-size:13.5px;line-height:20px}
.field{background:var(--field);border:1px solid rgba(255,255,255,.2);border-radius:4px;color:#dfe9f8;font-size:14px;padding:0 22px;display:flex;align-items:center}
.field.message{align-items:flex-start;padding-top:18px}
.btn-submit{left:520px;top:3992px;width:180px;height:40px;line-height:40px;background:#fff;color:var(--navy);font-size:15px}

/* footer */
.footer{left:0;top:4113px;width:1200px;height:342px;background:var(--footer);color:var(--footer-text)}
.footer h4{font-family:"Montserrat",Arial,sans-serif;color:#fff;font-size:14px;font-weight:700;text-transform:uppercase;margin-bottom:18px}
.footer ul{list-style:none}
.footer li{font-size:12.5px;line-height:22px}
.contact-list li{display:flex;gap:10px;align-items:flex-start;margin-bottom:8px;line-height:17px}
.social li{display:flex;gap:10px;align-items:center;margin-bottom:7px}
.social .dot{width:20px;height:20px;border-radius:50%;background:#fff;flex:none}
.copyright{left:0;top:4412px;width:1200px;text-align:center;font-size:11px;color:#8c8f95}
.footer-rule{left:0;top:4395px;width:1200px;height:1px;background:#34363a}
</style>
</head>
<body>
<div class="page">

  <!-- HERO -->
  <div class="abs hero-bg" role="img" aria-label="Blue tinted background photo of a team working with devices"></div>
  <div class="abs logo" style="left:132px;top:26px"><span class="mark"></span>TRELLFORM482</div>
  <nav class="abs nav">
    <a href="#" class="active">HOME</a><a href="#">APPS</a><a href="#">PRICING</a><a href="#">ADAPTER</a><a href="#">CONTACT</a>
  </nav>
  <h1 class="abs hero-title">Trellform482 syncs<br>your tools along<br>with your processes</h1>
  <p class="abs hero-text">Lorem ipsum dolor sit amet consectetuer adipiscing elit Nam cursus Morbi ut mi Nullam enim leo egestas</p>
  <div class="abs hero-btns"><a class="btn btn-white" href="#">Learn more</a><a class="btn btn-orange" href="#">Get started</a></div>
  <div class="abs hero-shot" role="img" aria-label="Screenshot of the process editor in a browser window"></div>
  <div class="abs hero-phone" role="img" aria-label="Mobile app screen with coloured app tiles"></div>
  <div class="abs slide-arrow" style="left:58px;top:290px"><svg width="14" height="14" viewBox="0 0 14 14"><path d="M9 2 4 7l5 5" stroke="#fff" stroke-width="2" fill="none"/></svg></div>
  <div class="abs slide-arrow" style="left:1102px;top:290px"><svg width="14" height="14" viewBox="0 0 14 14"><path d="M5 2l5 5-5 5" stroke="#fff" stroke-width="2" fill="none"/></svg></div>
  <svg class="abs" style="left:0;top:500px" width="1200" height="160" viewBox="0 0 1200 160">
    <path d="M0 130 Q420 40 760 70 T1200 20 L1200 160 L0 160 Z" fill="#fff"/>
    <path d="M0 130 Q420 40 760 70 T1200 20" fill="none" stroke="var(--orange)" stroke-width="8"/>
  </svg>

  <!-- CARDS -->
  <div class="abs card is-featured" style="left:128px">
    <svg width="96" height="96" viewBox="0 0 96 96"><circle cx="48" cy="48" r="40" fill="none" stroke="#fff" stroke-width="5"/><circle cx="48" cy="48" r="14" fill="none" stroke="#fff" stroke-width="5"/><circle cx="70" cy="28" r="6" fill="#fff"/></svg>
    <h3>Model processes</h3>
    <p>Lorem ipsum dolor sit amet consectetuer adipiscing elit Nam cursus Morbi ut mi Nullam enim leo egestas id condimentum at laoreet</p>
    <a class="btn btn-light" href="#">Learn More</a>
  </div>
  <div class="abs card" style="left:452px">
    <svg width="96" height="96" viewBox="0 0 96 96"><circle cx="48" cy="48" r="40" fill="none" stroke="var(--blue)" stroke-width="5"/><circle cx="48" cy="48" r="14" fill="none" stroke="var(--blue)" stroke-width="5"/><circle cx="70" cy="28" r="6" fill="var(--orange)"/></svg>
    <h3>Execute processes</h3>
    <p>Lorem ipsum dolor sit amet consectetuer adipiscing elit Nam cursus Morbi ut mi Nullam enim leo egestas id condimentum at laoreet</p>
    <a class="btn btn-navy" href="#">Learn More</a>
  </div>
  <div class="abs card" style="left:776px">
    <svg width="96" height="96" viewBox="0 0 96 96"><circle cx="48" cy="48" r="40" fill="none" stroke="var(--blue)" stroke-width="5"/><path d="M30 42a18 18 0 0 1 34-4M66 54a18 18 0 0 1-34 4" fill="none" stroke="var(--blue)" stroke-width="5"/><circle cx="70" cy="28" r="6" fill="var(--orange)"/></svg>
    <h3>Sync tools</h3>
    <p>Lorem ipsum dolor sit amet consectetuer adipiscing elit Nam cursus Morbi ut mi Nullam enim leo egestas id condimentum at laoreet</p>
    <a class="btn btn-navy" href="#">Learn More</a>
  </div>

  <!-- DIGITALIZATION -->
  <div class="abs media" style="left:140px;top:1005px;width:440px;height:268px;background:linear-gradient(135deg,#dfe5ec,#7d8fa6)" role="img" aria-label="Video still of a person at a desk in front of monitors"></div>
  <svg class="abs" style="left:326px;top:1105px" width="68" height="68" viewBox="0 0 68 68"><circle cx="34" cy="34" r="32" fill="#fff"/><path d="M27 21v26l21-13z" fill="#111"/></svg>
  <div class="abs split" style="left:630px;top:1018px;width:440px">
    <h2>Digitalization has become reality – not just a vision</h2>
    <p>Digitalization is not a new IT solution, a large tool platform, a complex suite or a new cloud offering – it means that you should use your existing tools along with your processes and your employees together with your clients and implement processes that ensure customer satisfaction by delivering cheaper, faster and better solutions.</p>
    <a class="btn btn-outline" href="#">Learn more</a>
  </div>

  <!-- FEATURES -->
  <svg class="abs" style="left:0;top:1330px" width="1200" height="540" viewBox="0 0 1200 540">
    <defs><linearGradient id="featBand" x1="0" y1="0" x2="1" y2="0"><stop offset="0" stop-color="#1f63bf"/><stop offset="1" stop-color="#0b3a8e"/></linearGradient></defs>
    <path d="M0 78 Q600 -10 1200 30 L1200 420 Q620 560 0 440 Z" fill="url(#featBand)"/>
    <path d="M0 440 Q620 560 1200 420" fill="none" stroke="var(--orange)" stroke-width="6"/>
  </svg>
  <h2 class="abs features-title">OUR FEATURES</h2>
  <svg class="abs" style="left:108px;top:1590px" width="24" height="40" viewBox="0 0 24 40"><path d="M20 4 4 20l16 16" stroke="#fff" stroke-width="3" fill="none" opacity=".7"/></svg>
  <svg class="abs" style="left:1058px;top:1590px" width="24" height="40" viewBox="0 0 24 40"><path d="M4 4l16 16L4 36" stroke="#fff" stroke-width="3" fill="none" opacity=".7"/></svg>
  <div class="abs feature" style="left:163px">
    <svg width="84" height="84" viewBox="0 0 84 84"><circle cx="42" cy="42" r="34" fill="none" stroke="#fff" stroke-width="5"/><circle cx="42" cy="42" r="12" fill="none" stroke="#fff" stroke-width="4"/><circle cx="62" cy="22" r="5" fill="var(--orange)"/></svg>
    <h3>Graphically model processes</h3>
    <p>We focus on visually attractive models, modelled with open standards. Your processes should be readable everywhere, not just to one tool.</p>
  </div>
  <div class="abs feature" style="left:380px">
    <svg width="84" height="84" viewBox="0 0 84 84"><circle cx="42" cy="42" r="34" fill="none" stroke="#fff" stroke-width="5"/><circle cx="42" cy="42" r="16" fill="none" stroke="#fff" stroke-width="4"/><path d="M26 42h32M42 26v32" stroke="#fff" stroke-width="3"/><circle cx="62" cy="22" r="5" fill="var(--orange)"/></svg>
    <h3>Rule-based sync</h3>
    <p>You define what data is synced to which system under which conditions. Rules and transfer profiles can be fully customized.</p>
  </div>
  <div class="abs feature" style="left:610px">
    <svg width="84" height="84" viewBox="0 0 84 84"><circle cx="42" cy="42" r="34" fill="none" stroke="#fff" stroke-width="5"/><path d="M30 30l12 12 12-12M42 42v14" stroke="#fff" stroke-width="4" fill="none"/><circle cx="30" cy="30" r="4" fill="#fff"/><circle cx="54" cy="30" r="4" fill="#fff"/><circle cx="42" cy="58" r="4" fill="#fff"/><circle cx="62" cy="22" r="5" fill="var(--orange)"/></svg>
    <h3>Tool Connection Wizard</h3>
    <p>It only takes a few clicks to integrate your tools into the platform. The Tool Connection Wizard helps you achieve your goals.</p>
  </div>
  <div class="abs feature" style="left:843px">
    <svg width="84" height="84" viewBox="0 0 84 84"><circle cx="42" cy="42" r="34" fill="none" stroke="#fff" stroke-width="5"/><rect x="31" y="26" width="22" height="30" rx="2" fill="none" stroke="#fff" stroke-width="4"/><path d="M36 36h12M36 44h12" stroke="#fff" stroke-width="3"/><circle cx="62" cy="22" r="5" fill="var(--orange)"/></svg>
    <h3>Documentation</h3>
    <p>Lorem ipsum dolor sit amet consectetuer adipiscing elit Nam cursus Morbi ut mi Nullam.</p>
  </div>

  <!-- PROCESSES -->
  <div class="abs split" style="left:160px;top:1948px;width:430px">
    <h2>Processes come to life – instead of being painted</h2>
    <p>Processes set the foundation for flexible and successful companies. Even though processes might be perceived as "bureaucratic" or "controlling people", our experience shows the opposite. Successful companies manage their processes proactively.</p>
    <a class="btn btn-outline" href="#">Learn more</a>
  </div>
  <div class="abs media" style="left:603px;top:1910px;width:447px;height:290px;background:linear-gradient(180deg,#f2f4f7,#dde2e9)" role="img" aria-label="Screenshot of the process editor with a workflow diagram"></div>

  <!-- TOOLS -->
  <div class="abs media" style="left:140px;top:2360px;width:440px;height:292px;background:linear-gradient(180deg,#f2f4f7,#dde2e9)" role="img" aria-label="Screenshot of the tool connection view with linked nodes"></div>
  <div class="abs split" style="left:630px;top:2378px;width:440px">
    <h2>Tools are in sync<br>without copy&amp;paste</h2>
    <p>Tools should support us in solving our tasks. But often they hinder us from being effective. You can find tools for almost any area where you use IT. Some of the tools are highly specialized for a specific purpose, others can be used very generically.</p>
    <a class="btn btn-outline" href="#">Learn more</a>
  </div>

  <!-- WORKFLOWS -->
  <div class="abs split" style="left:151px;top:2822px;width:430px">
    <h2>Relevant workflows are executed and monitored</h2>
    <p>Data is stored in several systems like ERP, CRM, PPS and many more. Many of these systems implement processes for various purposes, but not always in the form the company needs it.</p>
    <a class="btn btn-outline" href="#">Learn more</a>
  </div>
  <div class="abs media" style="left:603px;top:2776px;width:447px;height:284px;background:linear-gradient(180deg,#f2f4f7,#dde2e9)" role="img" aria-label="Screenshot of the workflow dashboard with coloured app tiles"></div>

  <!-- CLIENTS + CONTACT BACKGROUND -->
  <svg class="abs" style="left:0;top:3130px" width="1200" height="983" viewBox="0 0 1200 983">
    <defs>
      <linearGradient id="contactBand" x1="0" y1="0" x2="0" y2="1"><stop offset="0" stop-color="#1f63bf"/><stop offset="1" stop-color="#0b3a8e"/></linearGradient>
      <linearGradient id="clientBand" x1="0" y1="0" x2="0" y2="1"><stop offset="0" stop-color="#fff"/><stop offset="1" stop-color="#eceef1"/></linearGradient>
    </defs>
    <rect x="0" y="150" width="1200" height="833" fill="url(#contactBand)"/>
    <path d="M0 60 Q600 -30 1200 80 L1200 400 Q600 520 0 380 Z" fill="url(#clientBand)"/>
    <path d="M0 60 Q600 -30 1200 80" fill="none" stroke="var(--orange)" stroke-width="7"/>
    <path d="M0 380 Q600 520 1200 400" fill="none" stroke="var(--orange)" stroke-width="6"/>
    <path d="M0 40 Q600 -60 1200 60 L1200 0 L0 0 Z" fill="#fff"/>
  </svg>
  <h2 class="abs clients-title">Digitalization with Trellform482 has<br>successfully landed in many companies</h2>
  <div class="abs clients">
    <span>Norvale</span><span>Brisken</span><span>Quellmoor</span><span>Ostrava Works</span><span>Tamberline</span>
  </div>

  <!-- CONTACT -->
  <h2 class="abs contact-title">CONTACT FORM</h2>
  <p class="abs contact-intro">Lorem ipsum dolor sit amet consectetuer adipiscing elit Nam cursus Morbi ut mi Nullam enim leo egestas id condimentum at</p>
  <div class="abs field" style="left:228px;top:3750px;width:370px;height:44px">First Name</div>
  <div class="abs field" style="left:608px;top:3750px;width:368px;height:44px">Last Name</div>
  <div class="abs field" style="left:228px;top:3808px;width:370px;height:44px">Email address</div>
  <div class="abs field" style="left:608px;top:3808px;width:368px;height:44px">Phone</div>
  <div class="abs field message" style="left:228px;top:3866px;width:748px;height:100px">Message</div>
  <a class="abs btn btn-submit" href="#">Submit</a>

  <!-- FOOTER -->
  <footer class="abs footer">
    <div class="abs logo" style="left:155px;top:70px;font-size:20px"><span class="mark" style="width:34px;height:34px"></span>TRELLFORM482</div>
    <div class="abs" style="left:425px;top:55px;width:190px">
      <h4>Contact us</h4>
      <ul class="contact-list">
        <li><svg width="12" height="14" viewBox="0 0 12 14"><path d="M6 0a5 5 0 0 0-5 5c0 4 5 9 5 9s5-5 5-9a5 5 0 0 0-5-5z" fill="#fff"/><circle cx="6" cy="5" r="2" fill="#1e1f22"/></svg><span>120 Orrin Lane #4B<br>Texas 75001 TX</span></li>
        <li><svg width="12" height="12" viewBox="0 0 12 12"><path d="M2 0h3l1 3-2 1a7 7 0 0 0 4 4l1-2 3 1v3c0 1-1 2-2 2A10 10 0 0 1 0 2c0-1 1-2 2-2z" fill="#fff"/></svg><span>555.014.2202</span></li>
        <li><svg width="13" height="10" viewBox="0 0 13 10"><rect x=".5" y=".5" width="12" height="9" fill="none" stroke="#fff"/><path d="M.5.5l6 5 6-5" fill="none" stroke="#fff"/></svg><span>info@trellform482.example</span></li>
      </ul>
    </div>
    <div class="abs" style="left:640px;top:55px">
      <h4>Company</h4>
      <ul><li>Home</li><li>About us</li><li>Features</li><li>Pricing</li><li>Contact</li></ul>
    </div>
    <div class="abs" style="left:787px;top:50px">
      <h4>Resources</h4>
      <ul><li>Events</li><li>How to Docs</li><li>Trellform482</li><li>Privacy Policy</li><li>Adapter</li></ul>
    </div>
    <div class="abs" style="left:938px;top:50px">
      <h4>Get in touch</h4>
      <ul class="social"><li><span class="dot"></span>Chirpline</li><li><span class="dot"></span>Kinfold</li><li><span class="dot"></span>Workmesh</li><li><span class="dot"></span>Lenslog</li></ul>
    </div>
  </footer>
  <div class="abs footer-rule"></div>
  <p class="abs copyright">© 2019 Trellform482. All rights reserved</p>

</div>
</body>
</html>
```